Christian Motorcycle club/ministry website

I need a website for my Christian Motorcycle Club/Ministry.

This will be a place for members to go, to reach out to the public, to post events, maybe a place to sell support items but not right now

The name of the club is Iron Pilgrims. I have a logo that I will provide that needs to be on the webpage.

No sport bikes pictures, only cruisers if any images are used.

We are similar to a regular bike club but our mission is to tell other bikers and people about God.

We should have a contact page as well as an online application form.

I would like it to have a tough look to it. Just because we're Christians we're still bikers.

No scantily dressed women pictures

I'm open to any ideas as I don't really know what it should look like so feel free to be very creative.

Should also have a page for club rules and by laws

This website is for a Motorcycle Club - like the Dust Wolves or The Drifters or The Vandrels or Kin of the Highway television show

We are Christians so we tell people about God but we ride big Motorcycles

We wear leather jackets and beards and are tough big guys with tattoos

Here are some links to show you ideas of what kind of webpage we want:
http://www.borvanex.com/glen/motorcycle/
http://www.layoutquarry.com/demo/48172.html
http://dremwickstudio.com/portfolio/FirstLords/index.html
http://dustwolvesnorthside.com/index.html
http://www.layoutquarry.com/flash-templates/5830.html
http://www.layoutquarry.com/flash-templates/8295.html
http://www.pagecrate-designs.com/400217593-Biker-club-Flash-template-website.html

Thank you all for you submissions, you are all very talented artists and did a great job!

I wish you all the best of luck,
Dale

Industry/Entity Type

Club

Requirements
Must have
• Our logo
Should not have
• undressed women, no sport bikes

```html
<!DOCTYPE html>
<html lang="en">
<head>
<meta charset="utf-8">
<title>Iron Pilgrims Motorcycle Ministry – Events</title>
<link rel="stylesheet" href="https://fonts.googleapis.com/css2?family=Cinzel:wght@700;900&family=Oswald:wght@400;500&family=Playfair+Display:ital,wght@1,400;1,700&family=Merriweather:wght@700&family=Cabin+Condensed:wght@500;600&display=swap">
<style>
:root{
  --bg:#050505;
  --smoke:#2a2a2a;
  --ember:#e2661c;
  --ember-dark:#8a2e0e;
  --flame:#f6a21c;
  --title:#f08a24;
  --silver:#cfcfcf;
  --date-red:#b3202a;
  --paper:#e9e3da;
  --paper-edge:#bdb3a5;
  --placeholder-line:#b4b4b4;
  --placeholder-badge:#b0b0b0;
  --zoom:#cd7f52;
  --zoom-ring:#b96a3f;
  --frame-peach:#f3d2bb;
  --text-light:#ffffff;
  --text-muted:#8a8a8a;
}
*{box-sizing:border-box;margin:0;padding:0}
html,body{width:1134px;height:1200px;overflow:hidden;background:var(--bg)}
.page{
  position:relative;width:1134px;height:1200px;overflow:hidden;
  background:
    radial-gradient(ellipse 520px 260px at 560px 80px,#3a3a3a 0%,rgba(30,30,30,.6) 45%,transparent 80%),
    radial-gradient(ellipse 460px 320px at 560px 620px,#1d1d1d 0%,transparent 75%),
    radial-gradient(ellipse 300px 200px at 120px 200px,#242424 0%,transparent 75%),
    var(--bg);
  font-family:"Oswald",sans-serif;color:var(--text-light);
}
/* header */
.club-mark{
  position:absolute;left:161px;top:20px;width:218px;height:240px;
  display:flex;flex-direction:column;align-items:center;justify-content:center;gap:12px;
}
.club-mark .dot{width:120px;height:120px;border-radius:50%;background:var(--ember-dark);}
.club-mark .name{font-family:"Oswald",sans-serif;font-weight:500;font-size:26px;color:var(--ember);text-transform:uppercase;letter-spacing:1px}
.site-title{
  position:absolute;left:430px;top:40px;width:540px;text-align:center;
  font-family:"Cinzel",serif;font-weight:900;font-size:66px;line-height:90px;color:var(--title);
  letter-spacing:-1px;white-space:nowrap;
}
.site-subtitle{
  position:absolute;left:480px;top:138px;width:450px;text-align:center;
  font-family:"Cinzel",serif;font-weight:700;font-size:34px;color:var(--silver);letter-spacing:1px;white-space:nowrap;
}
.main-nav{
  position:absolute;left:406px;top:191px;width:586px;height:45px;
  background:linear-gradient(180deg,#b2461a 0%,#7b2a0d 55%,#5a1d08 100%);
  border-top:2px solid #d7743a;
  display:flex;align-items:center;
}
.main-nav a{
  font-family:"Oswald",sans-serif;font-size:17px;color:#f3e4d6;text-decoration:none;text-transform:uppercase;
  position:absolute;top:11px;line-height:22px;
}
.main-nav a.active{
  color:#fff;background:#2b140a;border-radius:14px;padding:0 12px;margin-left:-12px;
}
/* banner */
.page-banner{
  position:absolute;left:96px;top:227px;width:941px;height:143px;
  background:var(--frame-peach);padding:9px 10px;
  border-radius:3px;
}
.page-banner .inner{position:relative;width:100%;height:100%;background:#000;overflow:hidden}
.page-banner h1{
  position:absolute;left:40px;top:40px;font-family:"Merriweather",serif;font-weight:700;font-size:38px;color:#d8d8d8;
}
.banner-photo{
  position:absolute;right:0;top:0;width:280px;height:100%;
  background:linear-gradient(90deg,#000 0%,#2c2c2c 40%,#4a4a4a 70%,#1a1a1a 100%);
}
/* pager */
.pager{
  position:absolute;left:652px;width:385px;height:24px;
}
.pager .rail{position:absolute;left:0;right:0;top:10px;height:5px;border-top:1px solid #555;border-bottom:1px solid #555;background:repeating-linear-gradient(90deg,#222 0 10px,#444 10px 14px)}
.pager .tab{
  position:absolute;left:155px;top:-6px;width:170px;height:30px;
  background:linear-gradient(180deg,#3e3e3e,#161616);border-radius:14px 14px 4px 4px;
  display:flex;align-items:center;justify-content:center;gap:10px;
  font-family:"Cabin Condensed",sans-serif;font-weight:600;font-size:17px;color:#fff;
}
.pager .sep{width:1px;height:14px;background:#777}
.pager svg{width:10px;height:12px;vertical-align:-1px}
/* events */
.event{position:absolute;top:438px;width:265px;text-align:center}
.event-date{font-family:"Playfair Display",serif;font-style:italic;font-size:28px;color:var(--date-red);line-height:30px}
.event-name{font-family:"Playfair Display",serif;font-style:italic;font-size:20px;color:#e6e6e6;line-height:26px}
.event-place{font-family:"Playfair Display",serif;font-style:italic;font-weight:700;font-size:15px;color:#dcdcdc;line-height:20px}
.event-card{
  position:absolute;top:529px;width:264px;height:407px;
  background:radial-gradient(ellipse at center,var(--paper) 60%,var(--paper-edge) 100%);
  border-radius:6px;
}
.event-card .photo{position:absolute;left:19px;top:26px;width:222px;height:341px;background:#fff;border:1px solid #cfcfcf}
.event-card .photo svg{position:absolute;inset:0;width:100%;height:100%}
.event-card.is-hover .photo{background:var(--zoom)}
.zoom-label{
  position:absolute;left:0;right:0;top:208px;text-align:center;
  font-family:"Cabin Condensed",sans-serif;font-weight:600;font-size:16px;color:#fff;
}
/* fire */
.fire-band{
  position:absolute;left:140px;top:975px;width:880px;height:175px;
  background:radial-gradient(ellipse 460px 140px at 50% 100%,#f6a21c 0%,#e2661c 35%,#7a2a08 65%,transparent 100%);
}
/* footer */
.copyright{position:absolute;left:180px;top:1167px;font-family:Arial,sans-serif;font-size:11px;color:var(--text-muted)}
.copyright strong{color:#bdbdbd;font-weight:700}
.follow{position:absolute;left:641px;top:1159px;display:flex;align-items:center;gap:14px}
.follow-label{font-family:"Oswald",sans-serif;font-size:17px;color:#bcbcbc;text-transform:uppercase}
.social{display:flex;align-items:center;gap:5px;font-family:"Oswald",sans-serif;font-size:13px;color:#bcbcbc}
.social i{display:block;width:14px;height:14px;background:#555}
</style>
</head>
<body>
<div class="page">
  <header>
    <div class="club-mark"><span class="dot"></span><span class="name">Iron Pilgrims</span></div>
    <div class="site-title">IRON PILGRIMS</div>
    <div class="site-subtitle">MOTORCYCLE MINISTRY</div>
    <nav class="main-nav">
      <a href="#" style="left:49px">Home</a>
      <a href="#" style="left:136px">Our Mission</a>
      <a href="#" style="left:264px">Gallery</a>
      <a href="#" class="active" style="left:366px">Events</a>
      <a href="#" style="left:460px">Contact Us</a>
    </nav>
  </header>

  <section class="page-banner">
    <div class="inner">
      <h1>Events</h1>
      <div class="banner-photo" role="img" aria-label="Photo of club riders on cruisers at night"></div>
    </div>
  </section>

  <div class="pager" style="top:400px">
    <div class="rail"></div>
    <div class="tab">
      <span><svg viewBox="0 0 10 12"><path d="M8 1 3 6l5 5" stroke="#fff" stroke-width="2.4" fill="none"/></svg> Back</span>
      <span class="sep"></span>
      <span>Next <svg viewBox="0 0 10 12"><path d="M2 1l5 5-5 5" stroke="#fff" stroke-width="2.4" fill="none"/></svg></span>
    </div>
  </div>

  <div class="event" style="left:111px">
    <div class="event-date">June 7,8,9 2013</div>
    <div class="event-name">ML&amp;R Brennick VP Centro</div>
    <div class="event-place">Charter Mexico City</div>
  </div>
  <div class="event" style="left:432px">
    <div class="event-date">June 7,8,9 2013</div>
    <div class="event-name">ML&amp;R Brennick VP Centro</div>
    <div class="event-place">Charter Mexico City</div>
  </div>
  <div class="event" style="left:749px">
    <div class="event-date">June 7,8,9 2013</div>
    <div class="event-name">ML&amp;R Brennick VP Centro</div>
    <div class="event-place">Charter Mexico City</div>
  </div>

  <div class="event-card" style="left:113px">
    <div class="photo">
      <svg viewBox="0 0 222 341" preserveAspectRatio="none">
        <path d="M0 0 222 341M222 0 0 341" stroke="#b4b4b4" stroke-width="1.5"/>
        <circle cx="111" cy="170" r="28" fill="#b0b0b0"/>
        <text x="111" y="167" text-anchor="middle" font-family="Playfair Display, serif" font-style="italic" font-weight="700" font-size="13" fill="#fff">Event</text>
        <text x="111" y="181" text-anchor="middle" font-family="Playfair Display, serif" font-style="italic" font-weight="700" font-size="13" fill="#fff">Image</text>
      </svg>
    </div>
  </div>
  <div class="event-card is-hover" style="left:435px">
    <div class="photo">
      <svg viewBox="0 0 222 341" preserveAspectRatio="none">
        <path d="M0 0 222 341M222 0 0 341" stroke="#b96a3f" stroke-width="1.5"/>
        <circle cx="111" cy="170" r="29" fill="#b96a3f"/>
        <circle cx="106" cy="165" r="13" fill="none" stroke="#fff" stroke-width="3"/>
        <path d="M100 165h12M106 159v12" stroke="#fff" stroke-width="3"/>
        <path d="M115 174l10 10" stroke="#fff" stroke-width="5" stroke-linecap="round"/>
      </svg>
      <div class="zoom-label">Click to zoom-in</div>
    </div>
  </div>
  <div class="event-card" style="left:751px">
    <div class="photo">
      <svg viewBox="0 0 222 341" preserveAspectRatio="none">
        <path d="M0 0 222 341M222 0 0 341" stroke="#b4b4b4" stroke-width="1.5"/>
        <circle cx="111" cy="170" r="28" fill="#b0b0b0"/>
        <text x="111" y="167" text-anchor="middle" font-family="Playfair Display, serif" font-style="italic" font-weight="700" font-size="13" fill="#fff">Event</text>
        <text x="111" y="181" text-anchor="middle" font-family="Playfair Display, serif" font-style="italic" font-weight="700" font-size="13" fill="#fff">Image</text>
      </svg>
    </div>
  </div>

  <div class="fire-band" role="img" aria-label="Flames rising across the bottom of the page"></div>

  <div class="pager" style="top:980px">
    <div class="rail"></div>
    <div class="tab">
      <span><svg viewBox="0 0 10 12"><path d="M8 1 3 6l5 5" stroke="#fff" stroke-width="2.4" fill="none"/></svg> Back</span>
      <span class="sep"></span>
      <span>Next <svg viewBox="0 0 10 12"><path d="M2 1l5 5-5 5" stroke="#fff" stroke-width="2.4" fill="none"/></svg></span>
    </div>
  </div>

  <footer>
    <p class="copyright">© Copyright 2012 <strong>Iron Pilgrims Motorcycle Ministry</strong>&nbsp; All Rights Reserved.</p>
    <div class="follow">
      <span class="follow-label">Folow us on</span>
      <span class="social"><i></i>Skylark</span>
      <span class="social"><i></i>Porchboard</span>
      <span class="social"><i></i>Reelhub</span>
    </div>
  </footer>
</div>
</body>
</html>
```